Art Exhibit Invitation Design

This is an exhibit invitation for a three-artist show. The final postcard will be 6X9 and placed in an envelope of 6 1/2 by 9 1/2. I have placed two logos we use (although the logo color is pink, it is possible that the color can be changed. The artists are Marla Quenby, Leona Whitcombe, and Rosalind Verhoff. The corresponding images are Leona (apple tree), Rosalind (green celadon), and Marla (Poppies). The show runs July 8 - Aug 25. The opening Reception is Saturday, July 8 from 3-5pm. I would like this done in Adobe InDesign. Since the postcard is being put in an envelope, information about the exhibit can be put on the back (no return address or stamp will be needed) .
The Pemberly Gallery is located at 2417 E Fenwick Ridge Rd, Yakima WA 98907. our phone is (509) 555-0193.
The exhibit title is Quiet Weather.
Leona works in Pastel, Marla is a painter, and Rosalnd is a ceramicist.

```html
<!DOCTYPE html>
<html lang="en">
<head>
<meta charset="utf-8">
<title>Quiet Weather – Exhibit Invitation</title>
<link rel="stylesheet" href="https://fonts.googleapis.com/css2?family=Archivo+Narrow:wght@700&family=Dosis:wght@300;400;700&display=swap">
<style>
  :root {
    --page: #ffffff;
    --cream: #fdf8ec;
    --pink: #e5198a;
    --ink: #1c1c1c;
    --white: #ffffff;
    --shadow: rgba(0, 0, 0, 0.35);
  }
  * { box-sizing: border-box; margin: 0; padding: 0; }
  html, body { width: 1200px; height: 461px; overflow: hidden; background: var(--page); }
  .canvas { position: relative; width: 1200px; height: 461px; }

  /* Front: three artist panels */
  .artist-strip {
    position: absolute; left: 26px; top: 15px; width: 557px; height: 420px;
    overflow: hidden; display: flex; gap: 4px; background: var(--page);
  }
  .artist-panel { position: relative; flex: 1; height: 100%; overflow: hidden; }
  .artwork { position: absolute; inset: 0; }
  .artwork--pastel { background: linear-gradient(170deg, #f0b9a6 0%, #9bb07a 40%, #5d7d3c 75%, #8aa35c 100%); }
  .artwork--celadon { background: radial-gradient(circle at 50% 45%, #d8ebdc 0%, #b9d8c6 50%, #8fb7a4 80%, #2d3a4a 100%); }
  .artwork--painting { background: linear-gradient(160deg, #e4b24e 0%, #d9572a 40%, #b8301e 60%, #2f4d2a 85%, #d9d2cc 100%); }
  .artist-surname, .artist-first {
    position: absolute; left: 0; right: 0; text-align: center; color: var(--white);
    font-family: "Archivo Narrow", "Arial Narrow", sans-serif; font-weight: 700; line-height: 1;
    white-space: nowrap;
  }
  .artist-surname { top: -4px; font-size: 32px; letter-spacing: 0.5px; }
  .artist-first { top: 26px; font-size: 17px; letter-spacing: 1px; opacity: 0.85; }
  .front-title {
    position: absolute; left: 0; right: 0; bottom: -16px; text-align: center;
    font-family: "Archivo Narrow", "Arial Narrow", sans-serif; font-weight: 700;
    font-size: 78px; line-height: 1; color: var(--white); opacity: 0.9;
    letter-spacing: 1px; white-space: nowrap;
  }

  /* Back: striped envelope-style card */
  .card {
    position: absolute; left: 612px; top: 15px; width: 556px; height: 420px;
    background: repeating-linear-gradient(45deg,
      var(--pink) 0 10px, var(--cream) 10px 20px, var(--ink) 20px 30px, var(--cream) 30px 40px);
    box-shadow: 8px 8px 10px var(--shadow);
  }
  .card-inner {
    position: absolute; inset: 18px; background: var(--cream);
    font-family: "Dosis", "Trebuchet MS", sans-serif; color: var(--ink);
  }
  .event-label { position: absolute; left: 14px; top: 42px; font-size: 18px; color: var(--pink); letter-spacing: 0.5px; }
  .event-title {
    position: absolute; left: 12px; top: 70px; width: 228px;
    font-size: 34px; font-weight: 300; line-height: 1; white-space: nowrap;
  }
  .event-date { position: absolute; left: 14px; top: 122px; font-size: 21px; color: var(--pink); }
  .divider { position: absolute; left: 249px; top: 10px; width: 2px; height: 160px; background: var(--ink); }
  .artist-list { position: absolute; left: 16px; top: 192px; list-style: none; }
  .artist-list li {
    width: 210px; font-size: 19px; letter-spacing: 0.5px; text-transform: uppercase;
    border-bottom: 2px solid var(--ink); padding: 0 0 1px 4px; margin-bottom: 22px;
  }
  .gallery-name {
    position: absolute; right: 30px; top: 62px; text-align: right;
    font-weight: 700; font-size: 17px; letter-spacing: 1px;
  }
  .gallery-address {
    position: absolute; right: 30px; top: 108px; text-align: right;
    font-size: 13.5px; line-height: 1.55; font-style: normal;
  }
</style>
</head>
<body>
<div class="canvas">
  <section class="artist-strip">
    <div class="artist-panel">
      <div class="artwork artwork--pastel" role="img" aria-label="Pastel of a flowering apple tree by Leona Whitcombe"></div>
      <span class="artist-surname">WHITCOMBE</span><span class="artist-first">LEONA</span>
    </div>
    <div class="artist-panel">
      <div class="artwork artwork--celadon" role="img" aria-label="Carved green celadon ceramic plate by Rosalind Verhoff"></div>
      <span class="artist-surname">VERHOFF</span><span class="artist-first">ROSALIND</span>
    </div>
    <div class="artist-panel">
      <div class="artwork artwork--painting" role="img" aria-label="Painting of poppies in a vase by Marla Quenby"></div>
      <span class="artist-surname">QUENBY</span><span class="artist-first">MARLA</span>
    </div>
    <div class="front-title">QUIET WEATHER</div>
  </section>

  <section class="card">
    <div class="card-inner">
      <p class="event-label">Grand Opening</p>
      <h1 class="event-title">QUIET WEATHER</h1>
      <p class="event-date">July 8&nbsp; / &nbsp;3-5pm</p>
      <div class="divider"></div>
      <ul class="artist-list">
        <li>Marla Quenby</li>
        <li>Rosalind Verhoff</li>
        <li>Leona Whitcombe</li>
      </ul>
      <p class="gallery-name">PEMBERLY</p>
      <address class="gallery-address">
        Pemberly Gallery&nbsp; 2417 E<br>
        Fenwick Ridge Rd Yakima WA 98907<br>
        (509) 555-0193
      </address>
    </div>
  </section>
</div>
</body>
</html>
```